Birch heating and cooling LLC van wrap

The van is a 2017 for cargoline medium roof. We have a heating and cooling company and are wanting to get the van wrapped I will put the picture of our logo in the uploaded files below. The company name is Birch heating and cooling LLC we do residential hvac and duct work. Some light commercial jobs. Insured licensed and bonded our license number is HVAC -AL#4085316 somewhere on the van wrap there has got to be a Valtor logo because we are Valtor dealers and they help pay for advertising but I don’t want their logo to big because we also install other brands of equipment as well. I’m wanting something professional but yet stick out. Looking for the rolling billboard

Industry/Entity Type

Hvac

Requirements
Must have
• Company name “Birch heating and cooling LLC “ phone number “205-555-0148” HVAC license #AL-4085316

```html
<!DOCTYPE html>
<html lang="en">
<head>
<meta charset="utf-8">
<title>Birch Heating and Cooling LLC – Van Wrap</title>
<link href="https://fonts.googleapis.com/css2?family=Poppins:wght@500;600;700&display=swap" rel="stylesheet">
<style>
  :root {
    --wrap-red: #d3202a;
    --wrap-blue: #1826a8;
    --wrap-white: #ffffff;
    --trim-black: #222326;
    --glass: #3a3d44;
    --tyre: #1b1b1d;
    --hub: #c9cbcf;
    --lamp: #c7ccd3;
    --tail: #b5141c;
    --ink: #111111;
    --page: #ffffff;
  }
  html, body {
    margin: 0;
    padding: 0;
    width: 1200px;
    height: 1200px;
    overflow: hidden;
    background: var(--page);
  }
  .wrap-sheet { display: block; width: 1200px; height: 1200px; }
  .fill-red { fill: var(--wrap-red); }
  .fill-blue { fill: var(--wrap-blue); }
  .fill-white { fill: var(--wrap-white); }
  .trim { fill: var(--trim-black); }
  .glass { fill: var(--glass); }
  .tyre { fill: var(--tyre); }
  .hubcap { fill: var(--hub); stroke: #9a9ca1; stroke-width: 2; }
  .headlamp { fill: var(--lamp); }
  .taillamp { fill: var(--tail); }
  .panel-seam { fill: none; stroke: rgba(0,0,0,.18); stroke-width: .8; }
  .type { font-family: "Poppins", Arial, sans-serif; }
  .headline { font-weight: 700; font-size: 40px; letter-spacing: .5px; }
  .amp { font-weight: 600; font-size: 13px; }
  .services { font-weight: 500; font-size: 12.5px; letter-spacing: 1px; }
  .phone { font-weight: 700; font-size: 25px; }
  .web { font-weight: 500; font-size: 9px; }
  .license { font-weight: 700; font-size: 8.5px; }
  .badge-ring-red { fill: none; stroke: var(--wrap-red); stroke-width: 5; }
  .badge-face { fill: var(--wrap-white); stroke: var(--wrap-blue); stroke-width: 4; }
  .badge-name { font-weight: 700; font-size: 30px; fill: var(--wrap-blue); }
  .badge-sub { font-weight: 700; font-size: 14px; fill: var(--wrap-blue); }
  .dealer-dot { fill: var(--ink); }
  .dealer-name { font-weight: 600; font-size: 13px; fill: var(--ink); }
  .dealer-line { font-weight: 500; font-size: 7px; fill: var(--ink); }
</style>
</head>
<body>
<svg class="wrap-sheet" viewBox="0 0 960 960" xmlns="http://www.w3.org/2000/svg" aria-label="Birch Heating and Cooling van wrap, two colour options">
  <defs>
    <clipPath id="van-body">
      <path d="M28,362 L30,300 Q34,266 88,246 L190,150 Q232,96 330,76 L882,62 Q916,62 926,92 L936,300 L936,372 Q936,392 914,392 L28,392 Z"/>
    </clipPath>
  </defs>

  <!-- Option A: red / white / blue diagonal -->
  <g class="van van-option-a" transform="translate(0,0)">
    <g clip-path="url(#van-body)">
      <rect class="fill-white" x="0" y="40" width="960" height="360"/>
      <path class="fill-red" d="M0,40 L380,40 Q372,200 366,392 L0,392 Z"/>
      <path class="fill-blue" d="M700,40 L960,40 L960,400 L565,400 Z"/>
      <rect class="trim" x="0" y="336" width="960" height="60"/>
      <path class="fill-white" d="M240,352 L370,352 L370,356 L240,356 Z"/>
      <path class="fill-blue" d="M580,352 L760,352 L760,358 L576,358 Z"/>
    </g>
    <path class="glass" d="M205,240 L268,158 Q285,140 352,134 L352,232 Z"/>
    <path class="glass" d="M92,246 L190,152 L200,160 L120,244 Z"/>
    <path class="headlamp" d="M48,262 L112,254 L104,280 L52,288 Z"/>
    <rect class="taillamp" x="924" y="220" width="12" height="64" rx="3"/>
    <path class="panel-seam" d="M362,80 L362,336 M615,70 L615,336 M920,80 L920,336"/>

    <g class="wheel"><circle class="tyre" cx="180" cy="392" r="54"/><circle class="hubcap" cx="180" cy="392" r="36"/></g>
    <g class="wheel"><circle class="tyre" cx="770" cy="392" r="54"/><circle class="hubcap" cx="770" cy="392" r="36"/></g>

    <g class="license-block type">
      <text class="license" x="162" y="268" text-anchor="middle" fill="var(--wrap-white)">HVAC</text>
      <text class="license" x="162" y="280" text-anchor="middle" fill="var(--wrap-white)">LICENSE #AL-4085316</text>
    </g>

    <g class="dealer-mark type">
      <circle class="dealer-dot" cx="262" cy="284" r="7"/>
      <text class="dealer-name" x="273" y="289" fill="var(--wrap-white)">Valtor</text>
      <text class="dealer-line" x="236" y="328">Comfort, engineered daily.</text>
    </g>

    <g class="company-badge type">
      <circle class="badge-ring-red" cx="495" cy="200" r="118"/>
      <circle class="badge-face" cx="495" cy="200" r="104"/>
      <text class="badge-name" x="495" y="200" text-anchor="middle">Birch</text>
      <text class="badge-sub" x="495" y="224" text-anchor="middle">Heating and Cooling, LLC</text>
    </g>

    <g class="service-copy type" fill="var(--wrap-white)">
      <text class="headline" x="790" y="130" text-anchor="middle">HEATING</text>
      <text class="amp" x="790" y="146" text-anchor="middle">&amp;</text>
      <text class="headline" x="790" y="185" text-anchor="middle">COOLING</text>
      <text class="services" x="795" y="209" text-anchor="middle">RESIDENTIAL &amp; COMMERCIAL</text>
      <text class="phone" x="792" y="272" text-anchor="middle">205-555-0148</text>
      <text class="web" x="792" y="287" text-anchor="middle">www.birchheatingandcoolingllc.com</text>
    </g>
  </g>

  <!-- Option B: white body with red roof swoop and blue lower band -->
  <g class="van van-option-b" transform="translate(0,446)">
    <g clip-path="url(#van-body)">
      <rect class="fill-white" x="0" y="40" width="960" height="360"/>
      <path class="fill-red" d="M40,262 L190,150 Q232,96 330,76 L492,70 Q408,110 382,230 L366,150 L200,160 L92,250 Z"/>
      <path class="fill-red" d="M578,334 Q606,250 700,234 L960,222 L960,231 L704,243 Q626,256 594,334 Z"/>
      <path class="fill-blue" d="M600,336 Q632,262 708,250 L960,238 L960,400 L552,400 Q574,362 600,336 Z"/>
      <path class="fill-red" d="M530,400 Q544,360 560,336 L572,336 Q556,362 544,400 Z"/>
      <rect class="trim" x="0" y="336" width="960" height="60"/>
      <path class="fill-red" d="M540,352 L552,352 L548,358 L536,358 Z"/>
      <path class="fill-blue" d="M560,352 L760,352 L760,358 L556,358 Z"/>
    </g>
    <path class="glass" d="M205,240 L268,158 Q285,140 352,134 L352,232 Z"/>
    <path class="glass" d="M92,246 L190,152 L200,160 L120,244 Z"/>
    <path class="headlamp" d="M48,262 L112,254 L104,280 L52,288 Z"/>
    <rect class="taillamp" x="924" y="220" width="12" height="64" rx="3"/>
    <path class="panel-seam" d="M362,80 L362,336 M615,70 L615,336 M920,80 L920,336"/>

    <g class="wheel"><circle class="tyre" cx="180" cy="392" r="54"/><circle class="hubcap" cx="180" cy="392" r="36"/></g>
    <g class="wheel"><circle class="tyre" cx="770" cy="392" r="54"/><circle class="hubcap" cx="770" cy="392" r="36"/></g>

    <g class="license-block type">
      <text class="license" x="162" y="268" text-anchor="middle" fill="var(--wrap-blue)">HVAC</text>
      <text class="license" x="162" y="280" text-anchor="middle" fill="var(--wrap-red)">LICENSE #AL-4085316</text>
    </g>

    <g class="dealer-mark type">
      <circle class="dealer-dot" cx="262" cy="284" r="7"/>
      <text class="dealer-name" x="273" y="289">Valtor</text>
      <text class="dealer-line" x="236" y="328">Comfort, engineered daily.</text>
    </g>

    <g class="company-badge type">
      <circle class="badge-ring-red" cx="495" cy="200" r="118"/>
      <circle class="badge-face" cx="495" cy="200" r="104"/>
      <text class="badge-name" x="495" y="200" text-anchor="middle">Birch</text>
      <text class="badge-sub" x="495" y="224" text-anchor="middle">Heating and Cooling, LLC</text>
    </g>

    <g class="service-copy type">
      <text class="headline" x="757" y="124" text-anchor="middle" fill="var(--wrap-red)">HEATING</text>
      <text class="amp" x="757" y="141" text-anchor="middle" fill="var(--wrap-red)">&amp;</text>
      <text class="headline" x="757" y="180" text-anchor="middle" fill="var(--wrap-blue)">COOLING</text>
      <text class="services" x="757" y="206" text-anchor="middle" fill="var(--wrap-blue)">RESIDENTIAL &amp; COMMERCIAL</text>
      <text class="phone" x="764" y="282" text-anchor="middle" fill="var(--wrap-white)">205-555-0148</text>
      <text class="web" x="764" y="297" text-anchor="middle" fill="var(--wrap-white)">www.birchheatingandcoolingllc.com</text>
    </g>
  </g>
</svg>
</body>
</html>
```